High end wine label at Austrian Winery

We are a traditional winery in Austria in region Burgenland. We are looking for a relaunch of our current wine label for our [vantor] series. It's a high end wine series at an upper price range. At the moment we have just two kinds of the label, one white one for the white wines and one black one for the red wines. This is a series of wine, white, red, sweet, sparkling and a top wine categories. So we need the same label, but in 4 different ways to distinguish the wines plus the sparkling. Maybe in color, patterns, ... or something else. The label should be very simple, including our new logo. It's also possible to make one label but we can splitting two parts of the label. The size of the label does not matter, need not be the same as now. It's a bit higher than a normal bottle. Additionally we need a back label with wine description and the wine dates on it.

Target Market(s)

private consumers and restaurants, no retailers

Colors

Designer to choose colors to be used in the design.

Requirements
Must have
• simple label with 4 different categories (red, white, sweet, top) plus Frizzante label, new logo integrated, high end label. Just logo, grape variety and [vantor] as text on the front label as text
Nice to have
• It's just good, if there'sa possibility to have different colors of each grape variety (about 10 different), but all the same style. top Wines should have an extraordinary design, but familiar with the others
Should not have
• no cheap look

```html
<!DOCTYPE html>
<html lang="en">
<head>
<meta charset="utf-8">
<title>Halden [vantor] Label Series</title>
<link href="https://fonts.googleapis.com/css2?family=Bodoni+Moda:opsz,wght@6..96,500&family=Pinyon+Script&display=swap" rel="stylesheet">
<style>
  :root {
    --bg: #ffffff;
    --cream: #f8f5ea;
    --dark: #241a17;
    --gold: #b8923a;
    --gold-light: #f1d98a;
    --gold-deep: #7a5a1c;
    --ink: #1e1a18;
    --ghost-light: #dcd9d2;
    --ghost-dark: #4a403c;
  }
  * { box-sizing: border-box; margin: 0; padding: 0; }
  html, body { width: 1200px; height: 1200px; overflow: hidden; background: var(--bg); }
  .series { position: relative; width: 1200px; height: 1200px; }

  .label {
    position: absolute;
    top: 568px;
    width: 148px; height: 294px;
    background: var(--cream);
    overflow: hidden;
    box-shadow: 0 5px 14px rgba(0,0,0,0.12);
  }
  .label--red { background: var(--dark); }
  .label--sparkling { top: 693px; width: 172px; height: 227px; }

  .band {
    position: absolute; left: 0; right: 0; height: 9px;
    background: linear-gradient(90deg, var(--gold-deep), var(--gold-light) 45%, var(--gold) 70%, var(--gold-deep));
  }
  .band--top { top: 0; }
  .band--bottom { bottom: 0; }

  .lockup {
    position: absolute; left: 0; right: 0; top: 70px;
    display: flex; align-items: center; justify-content: center; gap: 7px;
  }
  .label--sparkling .lockup { top: 50px; }
  .lockup-dot {
    width: 11px; height: 11px; border-radius: 50%;
    background: var(--gold);
  }
  .brand {
    font-family: "Bodoni Moda", serif; font-weight: 500;
    font-size: 17px; letter-spacing: 1px; line-height: 1;
    color: var(--gold);
  }
  .tagline {
    position: absolute; left: 0; right: 0; top: 94px;
    text-align: center;
    font-family: "Bodoni Moda", serif; font-weight: 500;
    font-size: 7px; letter-spacing: 0.6px;
    color: var(--gold);
  }
  .label--sparkling .tagline { top: 74px; }

  .initial {
    position: absolute; left: 0; right: 0; top: 118px;
    text-align: center;
    font-family: "Pinyon Script", cursive;
    font-size: 150px; line-height: 1;
    color: var(--ghost-light);
  }
  .label--red .initial { color: var(--ghost-dark); }
  .label--sparkling .initial { top: 108px; left: -50px; font-size: 105px; }

  .variety {
    position: absolute; left: 12px; right: 12px; top: 154px;
    padding: 3px 0 2px;
    border-top: 1px solid var(--ink);
    border-bottom: 1px solid var(--ink);
    text-align: center; white-space: nowrap;
    font-family: "Bodoni Moda", serif; font-weight: 500;
    font-size: 12.5px; line-height: 1.2;
    color: var(--ink);
  }
  .variety-text { display: inline-block; transform: scaleX(0.82); }
  .label--red .variety { color: var(--gold); border-color: var(--gold); }
  .label--sparkling .variety { top: 132px; left: 26px; right: 26px; font-size: 17px; }

  .series-name {
    position: absolute; left: 0; right: 0; bottom: 20px;
    text-align: center;
    font-family: "Pinyon Script", cursive;
    font-size: 11px; color: var(--ink);
  }
  .label--red .series-name { color: var(--gold); }
  .label--sparkling .series-name { bottom: 18px; font-size: 13px; }
</style>
</head>
<body>
<main class="series">
  <section class="label label--red" style="left:94px;">
    <div class="band band--top"></div>
    <div class="lockup"><span class="lockup-dot"></span><span class="brand">HALDEN</span></div>
    <div class="tagline">BURGENLAND ESTATE</div>
    <div class="initial">B</div>
    <div class="variety"><span class="variety-text">BLAUFRÄNKISCH</span></div>
    <div class="series-name">[vantor]</div>
    <div class="band band--bottom"></div>
  </section>

  <section class="label label--white" style="left:311px;">
    <div class="band band--top"></div>
    <div class="lockup"><span class="lockup-dot"></span><span class="brand">HALDEN</span></div>
    <div class="tagline">BURGENLAND ESTATE</div>
    <div class="initial">G</div>
    <div class="variety"><span class="variety-text">GRÜNER VELTLINER</span></div>
    <div class="series-name">[vantor]</div>
    <div class="band band--bottom"></div>
  </section>

  <section class="label label--white" style="left:528px;">
    <div class="band band--top"></div>
    <div class="lockup"><span class="lockup-dot"></span><span class="brand">HALDEN</span></div>
    <div class="tagline">BURGENLAND ESTATE</div>
    <div class="initial">W</div>
    <div class="variety"><span class="variety-text">WELSCHRIESLING</span></div>
    <div class="series-name">[vantor]</div>
    <div class="band band--bottom"></div>
  </section>

  <section class="label label--white" style="left:737px;">
    <div class="band band--top"></div>
    <div class="lockup"><span class="lockup-dot"></span><span class="brand">HALDEN</span></div>
    <div class="tagline">BURGENLAND ESTATE</div>
    <div class="initial">P</div>
    <div class="variety"><span class="variety-text">PINOT BLANC</span></div>
    <div class="series-name">[vantor]</div>
    <div class="band band--bottom"></div>
  </section>

  <section class="label label--sparkling" style="left:956px;">
    <div class="band band--top"></div>
    <div class="lockup"><span class="lockup-dot"></span><span class="brand">HALDEN</span></div>
    <div class="tagline">BURGENLAND ESTATE</div>
    <div class="initial">F</div>
    <div class="variety"><span class="variety-text">FRIZZANTE</span></div>
    <div class="series-name">[vantor]</div>
    <div class="band band--bottom"></div>
  </section>
</main>
</body>
</html>
```